FR banner

we need a banner design (36"x120" horizontal) that will be displayed on a local high school baseball field. My company ( Crestwell Prints Co) has been producing signage for the Fernmoor Ridge community since 2009. We would like to communicate that we do more than banners. The final design should include the slogan "Signs Shirts Swag" and our Logo.

Target Market(s)

companies, teams, events, shirt and other marketing items.

Industry/Entity Type

Sign, Print,

Font styles to use
Sans Serif

Requirements
Should not have
• no baseball content.

```html
<!DOCTYPE html>
<html lang="en">
<head>
<meta charset="utf-8">
<title>Crestwell Prints Co — Signs Shirts Swag</title>
<link rel="stylesheet" href="https://fonts.googleapis.com/css2?family=Titan+One&display=swap">
<style>
  :root {
    --bg: #fdc500;
    --ghost: #f8af00;
    --ink: #111111;
    --shadow: #4a3a14;
    --signs: #e01e14;
    --shirts: #6fa3d2;
    --swag: #5a9a35;
  }
  html, body {
    margin: 0;
    padding: 0;
    width: 1200px;
    height: 360px;
    overflow: hidden;
    background: var(--bg);
  }
  .banner {
    position: relative;
    width: 1200px;
    height: 360px;
    background: var(--bg);
    font-family: "Titan One", "Arial Black", sans-serif;
  }
  .banner svg {
    position: absolute;
    inset: 0;
    width: 1200px;
    height: 360px;
  }
  .slogan-ghost { fill: var(--ghost); }
  .slogan-shadow { fill: var(--shadow); }
  .word-signs { fill: var(--signs); }
  .word-shirts { fill: var(--shirts); }
  .word-swag { fill: var(--swag); }
  .brand-name { fill: var(--ink); }
  .brand-mark { fill: var(--ink); }
</style>
</head>
<body>
<main class="banner">
  <svg viewBox="0 0 1200 360" xmlns="http://www.w3.org/2000/svg" font-family="'Titan One', 'Arial Black', sans-serif">
    <!-- brand block -->
    <g class="brand">
      <rect class="brand-mark" x="24" y="86" width="22" height="22"/>
      <text class="brand-name" x="24" y="160" font-size="48" textLength="232" lengthAdjust="spacingAndGlyphs">CRESTWELL</text>
      <text class="brand-name" x="24" y="218" font-size="48" textLength="232" lengthAdjust="spacingAndGlyphs">PRINTS</text>
      <text class="brand-name" x="24" y="276" font-size="48" textLength="84" lengthAdjust="spacingAndGlyphs">CO</text>
    </g>

    <!-- faint top row -->
    <text class="slogan-ghost" x="287" y="95" font-size="88" textLength="873" lengthAdjust="spacingAndGlyphs">SIGNS SHIRTS SWAG</text>

    <!-- main slogan -->
    <g class="slogan">
      <text class="slogan-shadow" x="287" y="207" font-size="88" textLength="869" lengthAdjust="spacingAndGlyphs">SIGNS SHIRTS SWAG</text>
      <text x="293" y="200" font-size="88" textLength="869" lengthAdjust="spacingAndGlyphs"><tspan class="word-signs">SIGNS </tspan><tspan class="word-shirts">SHIRTS </tspan><tspan class="word-swag">SWAG</tspan></text>
    </g>

    <!-- faint bottom row -->
    <text class="slogan-ghost" x="287" y="321" font-size="88" textLength="873" lengthAdjust="spacingAndGlyphs">SIGNS SHIRTS SWAG</text>
  </svg>
</main>
</body>
</html>
```